For Sale Poster Design

We need a beautiful and tropical looking FOR SALE poster for our speed boat.

Poster format need to be 297x420mm / 300dpi
PSD with all layers.

The photos from the boat can be downloaded here: www.korvado.nl/photos.zip

Target Market(s)

Tourists, expats

Requirements
Must have
• The poster need to have the following text:

Speed Boat Sale

This beautiful full glass fiber speedboat (location Lombok, Indonesia) is perfect for tropical conditions: island transfer, diving, wake boarding, fishing, private charters and leisure activities.

The newly bought 2x 200 HP TORUMI 4 Stroke (2013) will give you an enormous power on the water with maximum speed of 40 Knot / 74 Km/hour. This will bring you from Lombok to Bali in just 50 minutes and only few minutes long from the famous tropical Gili islands.

The speedboat also has the comfort of a small cabin with skylight, sun controlled ventilation system, a small bed, a toilet and a fridge. There are 16 seats in the open section of the boat. The boat is equipped with modern brand-new GPS, Sonar and an FM / AM Radio system.

This speedboat was built in 2011 and is meticulously maintained to the highest standard. It comes with a captain and boatman.

Specs:
Overall length: 11 Meter 36 feet.
Built year: 2011, Bali
Engines: 2x 200 HP TORUMI 4 Stroke (Bought 2013)
Capacity: Max. 16 People (Incl. Crew)
Max speed: 40 Knot / 74 Km/hour
GPS / Sonar: Pelcorn RM-42TX
Tankage: 300 Liter
Lighting: LED / Halogen

Price 99.000 USD
Nice to have
• Big FOR SALE banner on the poster

```html
<!DOCTYPE html>
<html lang="en">
<head>
<meta charset="utf-8">
<title>Speed Boat Sale</title>
<link href="https://fonts.googleapis.com/css2?family=Racing+Sans+One&family=Open+Sans:wght@400;600&family=Roboto+Condensed:wght@400;700&display=swap" rel="stylesheet">
<style>
  :root {
    --navy-deep: #041a4a;
    --navy: #0a2f80;
    --blue: #1560c4;
    --sky: #3a8fe0;
    --panel: rgba(8, 30, 90, 0.85);
    --panel-edge: rgba(120, 170, 240, 0.45);
    --gold-light: #fff1b8;
    --gold: #e2b24a;
    --gold-dark: #8a5a14;
    --ring: #c79a4a;
    --white: #ffffff;
    --yellow: #ffe23a;
  }
  * { margin: 0; padding: 0; box-sizing: border-box; }
  html, body { width: 849px; height: 1200px; overflow: hidden; background: #fff; }
  .poster {
    position: relative;
    width: 849px;
    height: 1200px;
    overflow: hidden;
    background: linear-gradient(180deg, var(--navy-deep) 0%, var(--navy) 25%, var(--blue) 55%, var(--sky) 78%, #8cc8f2 86%);
    font-family: "Open Sans", sans-serif;
    color: var(--white);
  }
  .title {
    position: absolute;
    top: 40px; left: 0; width: 100%;
    text-align: center;
    font-family: "Racing Sans One", sans-serif;
    font-size: 84px;
    font-variant: small-caps;
    font-style: italic;
    letter-spacing: 4px;
    line-height: 1;
    background: linear-gradient(180deg, var(--gold-light) 0%, var(--gold) 45%, var(--gold-dark) 55%, var(--gold) 80%, var(--gold-light) 100%);
    -webkit-background-clip: text;
    background-clip: text;
    color: transparent;
    filter: drop-shadow(2px 3px 2px rgba(0,0,0,0.6));
  }
  .beach-scene {
    position: absolute;
    left: 0; top: 1000px; width: 849px; height: 200px;
    z-index: 1;
    background: linear-gradient(180deg, #9fd3f3 0%, #cfe9f3 20%, #2fc2c9 42%, #19a7b6 62%, #e9dcc0 85%, #d9c8a2 100%);
  }
  .photo-circle {
    position: absolute;
    border-radius: 50%;
    border: 9px solid var(--ring);
    box-shadow: 0 0 0 2px #f4dba0, 0 6px 14px rgba(0,0,0,0.45);
    z-index: 3;
  }
  .photo-cockpit {
    left: 8px; top: 175px; width: 404px; height: 404px;
    background: radial-gradient(circle at 50% 40%, #f6f4ee 0%, #e8e0cc 45%, #c7ad7c 75%, #9c8660 100%);
  }
  .photo-cabin {
    left: 485px; top: 638px; width: 352px; height: 352px;
    background: radial-gradient(circle at 55% 35%, #ffffff 0%, #eeeae2 45%, #d2bb8a 75%, #a58c60 100%);
  }
  .panel {
    position: absolute;
    background: var(--panel);
    border: 1px solid var(--panel-edge);
    border-radius: 22px;
    z-index: 2;
  }
  .intro {
    left: 402px; top: 172px; width: 422px; height: 470px;
    padding: 18px 20px 12px 26px;
    font-size: 14px;
    line-height: 21px;
    text-align: justify;
  }
  .intro p + p { margin-top: 14px; }
  .specs-heading {
    position: absolute;
    left: 26px; top: 672px;
    z-index: 2;
    font-family: "Racing Sans One", sans-serif;
    font-style: italic;
    font-size: 52px;
    line-height: 1;
    background: linear-gradient(180deg, var(--gold-light) 0%, var(--gold) 50%, var(--gold-dark) 58%, var(--gold) 100%);
    -webkit-background-clip: text;
    background-clip: text;
    color: transparent;
    filter: drop-shadow(2px 2px 2px rgba(0,0,0,0.6));
  }
  .specs {
    left: 14px; top: 735px; width: 424px; height: 256px;
    padding: 22px 10px 0 30px;
    font-family: "Roboto Condensed", sans-serif;
    font-size: 16px;
  }
  .spec-list { list-style: none; }
  .spec-list li {
    display: grid;
    grid-template-columns: 14px 108px 16px 1fr;
    line-height: 24px;
  }
  .spec-list li::before { content: "•"; font-weight: 700; }
  .spec-label { font-weight: 700; }
  .price-burst {
    position: absolute;
    left: 330px; top: 910px; width: 210px; height: 210px;
    z-index: 4;
    filter: drop-shadow(2px 4px 4px rgba(0,0,0,0.45));
  }
  .price-text {
    position: absolute;
    left: 330px; top: 910px; width: 210px; height: 210px;
    z-index: 5;
    display: flex; flex-direction: column; align-items: center; justify-content: center;
    transform: rotate(-22deg);
    font-family: "Racing Sans One", sans-serif;
    color: var(--yellow);
    line-height: 0.95;
    text-shadow: 1px 2px 2px rgba(0,0,0,0.5);
  }
  .price-label { font-size: 46px; }
  .price-amount { font-size: 30px; margin-top: 4px; }
  .price-currency { font-size: 26px; }
</style>
</head>
<body>
<main class="poster">
  <h1 class="title">Speed Boat Sale</h1>

  <div class="beach-scene" role="img" aria-label="Photo of the speed boat anchored at a tropical beach with turquoise water and palm trees"></div>

  <div class="photo-circle photo-cockpit" role="img" aria-label="Photo of the speed boat cockpit with cream seats and steering console"></div>

  <section class="panel intro">
    <p>This beautiful full glass fiber speed boat (location Lombok, Indonesia) is perfect for tropical conditions. Island transfer, diving, wake boarding, fishing, private charters and leisure features.</p>
    <p>The new (2013) bought 2x 200 HP TORUMI 4 Stroke will give you an enormous power on the water with maximum speed of 40 Knot / 74 Km/hour and will bring you within only 50 minutes from Lombok to Bali and within minute distance from all famous tropical Gili islands.</p>
    <p>The speed boat also has the comfort of a small cabin with skylight, sun controlled ventilation system, a small bed, a toilet and a fridge. In the open section of the boat are 16 seats, besides all of this is the boat equipped with brand-new GPS, Sonar and an FM / AM Radio system.</p>
    <p>This boat was built in 2011 and it was meticulously maintained to the highest standard.</p>
  </section>

  <h2 class="specs-heading">Specs:</h2>
  <section class="panel specs">
    <ul class="spec-list">
      <li><span class="spec-label">Overall length</span><span>:</span><span>11 Meter 36 feet.</span></li>
      <li><span class="spec-label">Built year</span><span>:</span><span>2011, Bali</span></li>
      <li><span class="spec-label">Engines</span><span>:</span><span>2x 200 HP TORUMI 4 Stroke<br>(Bought 2013)</span></li>
      <li><span class="spec-label">Capacity</span><span>:</span><span>Max. 16 People (Incl. Crew)</span></li>
      <li><span class="spec-label">Max speed</span><span>:</span><span>40 Knot / 74 Km/hour</span></li>
      <li><span class="spec-label">GPS / Sonar</span><span>:</span><span>Pelcorn RM-42TX</span></li>
      <li><span class="spec-label">Tankage</span><span>:</span><span>300 Liter</span></li>
      <li><span class="spec-label">Lighting</span><span>:</span><span>LED / Halogen</span></li>
    </ul>
  </section>

  <div class="photo-circle photo-cabin" role="img" aria-label="Photo of the boat cabin interior with bench seat and windows"></div>

  <svg class="price-burst" viewBox="0 0 200 200" aria-hidden="true">
    <defs>
      <radialGradient id="burstFill" cx="50%" cy="45%" r="55%">
        <stop offset="0%" stop-color="#f23a2a"/>
        <stop offset="100%" stop-color="#a80808"/>
      </radialGradient>
    </defs>
    <polygon fill="url(#burstFill)" stroke="#ffffff" stroke-width="3"
      points="200,100 178.5,115.6 192.4,138.3 166.5,144.5 170.7,170.7 144.5,166.5 138.3,192.4 115.6,178.5 100,200 84.4,178.5 61.7,192.4 55.5,166.5 29.3,170.7 33.5,144.5 7.6,138.3 21.5,115.6 0,100 21.5,84.4 7.6,61.7 33.5,55.5 29.3,29.3 55.5,33.5 61.7,7.6 84.4,21.5 100,0 115.6,21.5 138.3,7.6 144.5,33.5 170.7,29.3 166.5,55.5 192.4,61.7 178.5,84.4"/>
  </svg>
  <div class="price-text">
    <span class="price-label">Price</span>
    <span class="price-amount">99,000</span>
    <span class="price-currency">USD</span>
  </div>
</main>
</body>
</html>
```